Moder Business Card Design for Renewables Business

Need a business card design for my business. We collect & repurpose spent coffee ground from cafes. The cards will be made from recycled paper. Needs to fit our corporate colour scheme of white, green & brown (see logo for colour codes). Eco friendly, modern, intresting & eye catching.
This card needs to convey the message of the business and fit into its mantra of eco-friendly, sustainable etc.

Target Market(s)

Cafe Owners, Coffee Drinkers, Recycling Companies, Farmers

Industry/Entity Type

Recycling

Contact Information for Business Card

Name; Peter Halloran
Phone; 0412 386 527
e-mail; info@lumatrove.com.au
website; www.lumatrove.com.au

Font styles to use
Sans Serif
Script

Colors

Designer to choose colors to be used in the design.

Requirements
Must have
• FRONT;
• Logo, Name (Peter Halloran), phone number, e-mail address, website
• BACK;
• On the back in cursive text; 'GOOD GROUNDS FOR A GREENER DAY'
• Small facebook & Instagram logos with text 'Lumatrove'
Should not have
• messy design

```html
<!DOCTYPE html>
<html lang="en">
<head>
<meta charset="utf-8">
<title>Lumatrove Business Card</title>
<link rel="stylesheet" href="https://fonts.googleapis.com/css2?family=Open+Sans:wght@600;700&family=Kaushan+Script&display=swap">
<style>
  :root {
    --backdrop: #2e2e2e;
    --paper: #ebe8e3;
    --leaf-green: #6ea23a;
    --bean-brown: #5e2f14;
    --white: #ffffff;
  }
  html, body {
    margin: 0;
    width: 1200px;
    height: 900px;
    overflow: hidden;
    background: var(--backdrop);
  }
  .sheet {
    position: relative;
    width: 1200px;
    height: 900px;
  }
  .card {
    position: absolute;
    top: 301px;
    width: 514px;
    height: 296px;
    display: block;
    filter: drop-shadow(0 4px 8px rgba(0,0,0,0.45));
  }
  .card--front { left: 72px; }
  .card--back { left: 614px; }
  .paper { fill: url(#paperTone); }
  .brand-ring { fill: none; stroke: var(--bean-brown); stroke-width: 5; }
  .brand-name {
    font-family: "Open Sans", Arial, sans-serif;
    font-weight: 600;
    font-size: 22px;
    fill: var(--leaf-green);
    letter-spacing: 0.2px;
  }
  .ground-band { fill: var(--bean-brown); }
  .tagline {
    font-family: "Kaushan Script", cursive;
    font-size: 19px;
    fill: var(--leaf-green);
  }
  .social-dot { fill: var(--white); }
  .social-handle {
    font-family: "Open Sans", Arial, sans-serif;
    font-weight: 600;
    font-size: 12px;
    fill: var(--white);
  }
  .divider { stroke: var(--bean-brown); stroke-width: 2; }
  .person {
    font-family: "Open Sans", Arial, sans-serif;
    font-weight: 700;
    font-size: 12.5px;
    fill: var(--bean-brown);
  }
  .contact {
    font-family: "Open Sans", Arial, sans-serif;
    font-weight: 600;
    font-size: 12.5px;
    fill: var(--bean-brown);
  }
  .icon-badge { fill: var(--leaf-green); }
  .icon-glyph { fill: none; stroke: var(--white); stroke-width: 1.2; }
  .icon-fill { fill: var(--white); }
</style>
</head>
<body>
<main class="sheet">
  <svg width="0" height="0" style="position:absolute" aria-hidden="true">
    <defs>
      <radialGradient id="paperTone" cx="50%" cy="45%" r="75%">
        <stop offset="0%" stop-color="#eeebe7"/>
        <stop offset="100%" stop-color="#e3dfd9"/>
      </radialGradient>
    </defs>
  </svg>

  <svg class="card card--front" viewBox="0 0 530 306" role="group" aria-label="Lumatrove card, tagline side">
    <rect class="paper" x="0" y="0" width="530" height="306"/>
    <circle class="brand-ring" cx="266" cy="140" r="57"/>
    <text class="brand-name" x="266" y="228" text-anchor="middle">LUMATROVE</text>

    <path class="ground-band" d="M76 306 Q271 236 466 306 Z"/>
    <path id="taglineArc" d="M124 281 Q268 244 412 266" fill="none"/>
    <text class="tagline">
      <textPath href="#taglineArc" startOffset="50%" text-anchor="middle">Good grounds for a greener day</textPath>
    </text>

    <circle class="social-dot" cx="232" cy="287" r="5"/>
    <text class="social-handle" x="243" y="291.5">LUMATROVE</text>
  </svg>

  <svg class="card card--back" viewBox="0 0 530 306" role="group" aria-label="Lumatrove card, contact side">
    <rect class="paper" x="0" y="0" width="530" height="306"/>
    <circle class="brand-ring" cx="129" cy="140" r="57"/>
    <text class="brand-name" x="129" y="228" text-anchor="middle">LUMATROVE</text>

    <line class="divider" x1="266" y1="78" x2="266" y2="229"/>

    <text class="person" x="302" y="112">PETER HALLORAN</text>
    <text class="person" x="302" y="130">MANAGING DIRECTOR</text>

    <g class="contact-row">
      <circle class="icon-badge" cx="309" cy="161" r="6"/>
      <path class="icon-fill" d="M305.5 158.5 q3.5 -2 7 0 v1.5 h-2 v-0.8 h-3 v0.8 h-2 z M306 161 h6 v2.8 h-6 z"/>
      <text class="contact" x="322" y="165.5">0412 386 527</text>
    </g>
    <g class="contact-row">
      <circle class="icon-badge" cx="309" cy="179" r="6"/>
      <rect class="icon-fill" x="305.3" y="176.3" width="7.4" height="5.4" rx="0.6"/>
      <path d="M305.5 176.8 L309 179.6 L312.5 176.8" fill="none" stroke="#6ea23a" stroke-width="0.9"/>
      <text class="contact" x="322" y="183.5">info@lumatrove.com.au</text>
    </g>
    <g class="contact-row">
      <circle class="icon-badge" cx="309" cy="197" r="6"/>
      <circle class="icon-glyph" cx="309" cy="197" r="3.7"/>
      <ellipse class="icon-glyph" cx="309" cy="197" rx="1.6" ry="3.7"/>
      <line class="icon-glyph" x1="305.3" y1="197" x2="312.7" y2="197"/>
      <text class="contact" x="322" y="201.5">www.lumatrove.com.au</text>
    </g>
  </svg>
</main>
</body>
</html>
```